Banner Ad Design Project

We need a server banner image for our web site. The banner is to sell dedicated servers. The size needs to be 732x138 pixels.

Here is an example of the background we're thinking about: http://www.quolventa.com/images/banners/qvbanner.png

But feel free to be creative, and design a banner that looks good on the following page: http://www.quolventa.com/marbexservers.asp

Incorporate some of these words in the banner as features:
-Rapid I/O SSD Hybrid RAID
-SLA Included
-Marbex Dorvo Processors
-24x7 Monitoring and Support

I like the colors on this banner... http://www.quolventa.com/images/banners/header-spring.png

so, maybe a white background would look good.

```html
<!DOCTYPE html>
<html lang="en">
<head>
<meta charset="utf-8">
<title>Dedicated Servers Banner</title>
<link href="https://fonts.googleapis.com/css2?family=Oswald:wght@600&display=swap" rel="stylesheet">
<style>
  :root {
    --sky-steel: #8aa6c4;
    --rack-blue: #2c4a78;
    --rack-deep: #0f1c36;
    --rack-night: #070d1c;
    --feature-text: #ffffff;
    --feature-glow: rgba(10, 25, 60, 0.9);
  }
  html, body {
    margin: 0;
    padding: 0;
    overflow: hidden;
    background: #ffffff;
  }
  .banner {
    position: relative;
    width: 1200px;
    height: 226px;
    overflow: hidden;
  }
  .server-backdrop {
    position: absolute;
    inset: 0;
    background:
      radial-gradient(ellipse 180px 120px at 120px 80px, rgba(200,220,240,0.55), transparent 70%),
      radial-gradient(ellipse 260px 90px at 900px 40px, rgba(120,160,210,0.35), transparent 70%),
      radial-gradient(ellipse 300px 100px at 1050px 200px, rgba(90,130,190,0.35), transparent 70%),
      linear-gradient(100deg, var(--sky-steel) 0%, var(--rack-blue) 22%, var(--rack-deep) 45%, var(--rack-night) 62%, var(--rack-deep) 82%, var(--rack-blue) 100%);
  }
  .feature-list {
    position: absolute;
    inset: 0;
    margin: 0;
    padding: 0;
    list-style: none;
    font-family: "Oswald", "Arial Narrow", sans-serif;
    font-weight: 600;
    font-size: 47px;
    line-height: 1;
    text-transform: uppercase;
    color: var(--feature-text);
    text-shadow: 0 0 6px var(--feature-glow), 1px 2px 3px var(--feature-glow);
    white-space: nowrap;
  }
  .feature {
    position: absolute;
  }
  .feature::before {
    content: "\2022";
    margin-right: 10px;
  }
  .feature-raid { left: 574px; top: 12px; }
  .feature-sla { left: 525px; top: 58px; }
  .feature-cpu { left: 476px; top: 107px; }
  .feature-support { left: 418px; top: 156px; }
</style>
</head>
<body>
  <div class="banner">
    <div class="server-backdrop" role="img" aria-label="Close-up photo of rack-mounted servers in blue light"></div>
    <ul class="feature-list">
      <li class="feature feature-raid">Rapid I/O SSD Hybrid RAID</li>
      <li class="feature feature-sla">SLA Included</li>
      <li class="feature feature-cpu">Marbex Dorvo Processors</li>
      <li class="feature feature-support">24x7 Monitoring and Support</li>
    </ul>
  </div>
</body>
</html>
```